Pack Your Bags! The TOP holiday homes in Colorado

This project is for a book cover/spine and back for a book A book featuring vacation rentals in the state of Colorado in the US. Arranged as one journey from beginning to end, sharing stories from each of the unique vacation rental hosts. The book takes you through their beginnings, how they overcame some of the common problems faced in the industry, and why they continue to love hosting guests from all over the world. You will feel as if you are right there with them, learning about their properties and getting a sense of what it's like to truly "live" in Colorado.

is easy to understand why so many people are drawn to the charm of Colorado’s vacation rentals. The unique and quality sanctuaries for travelers and locals alike offer some of the best views, most luxurious amenities, and prime locations that can be found.
But what goes on behind the scenes? How do these exclusive vacation rentals maintain their unique flare, how do they provide such high quality customer service and why are people willing to pay so much for a vacation rental?”

Some areas are close to abandoned ski resorts while others are secluded getaways that have been converted into luxury residences. From rustic to luxurious, each of these properties offers a one-of-a-kind vacation experience. Whether you are looking for a place to stay during a ski trip or want to explore the state's natural wonders, there is something for everyone in this book. So, pack your bags!

There are no current images of the vacation rentals as they have not been selected yet so this cover should reflect the theme of the book without focusing on a particular property.

```html
<!DOCTYPE html>
<html lang="en">
<head>
<meta charset="utf-8">
<title>Pack Your Bags! – Book Cover</title>
<link rel="stylesheet" href="https://fonts.googleapis.com/css2?family=Alegreya:wght@400;800&family=Archivo:ital,wght@0,500;0,600;1,600&display=swap">
<style>
  :root {
    --coral: #d65f58;
    --ink: #1d1515;
    --paper: #ffffff;
    --sky: #b4a0a6;
    --peak: #e3968c;
    --rock: #c4602f;
    --snow: #cbc3c5;
    --scrub: #6f6a5c;
  }
  * { margin: 0; padding: 0; box-sizing: border-box; }
  html, body { width: 1200px; height: 849px; overflow: hidden; background: var(--paper); }
  .cover { position: relative; width: 1200px; height: 849px; }

  /* Back cover */
  .back { position: absolute; left: 0; top: 0; width: 583px; height: 849px; background: var(--coral); color: var(--ink); }
  .back__photo {
    position: absolute; left: 71px; top: 77px; width: 157px; height: 197px;
    border-radius: 50% 50% 48% 48% / 42% 42% 40% 40%;
    background:
      radial-gradient(ellipse 40% 35% at 30% 50%, var(--rock) 0%, rgba(196,96,47,0) 100%),
      linear-gradient(180deg, var(--sky) 0%, var(--peak) 22%, var(--snow) 45%, #b9a9a6 70%, var(--scrub) 100%);
  }
  .back__intro {
    position: absolute; left: 268px; top: 101px; width: 245px;
    font: 500 10.3px/18.7px "Archivo", sans-serif; text-align: justify;
  }
  .divider { position: absolute; left: 105px; width: 374px; height: 18px; }
  .divider--top { top: 357px; }
  .divider--bottom { top: 556px; }
  .back__quote {
    position: absolute; left: 105px; width: 374px; text-align: center;
    font: italic 600 12px/18.8px "Archivo", sans-serif; letter-spacing: 2.9px;
  }
  .back__quote--first { top: 401px; }
  .back__quote--second { top: 616px; }

  /* Spine */
  .spine { position: absolute; left: 583px; top: 0; width: 34px; height: 849px; background: var(--paper); }
  .spine__title {
    position: absolute; left: 17px; top: 540px;
    transform: translate(-50%, -50%) rotate(-90deg);
    white-space: nowrap; font: 500 14.6px/1 "Archivo", sans-serif; color: var(--ink);
  }
  .spine__star { position: absolute; left: 9px; top: 808px; width: 16px; height: 16px; }

  /* Front cover */
  .front { position: absolute; left: 617px; top: 0; width: 583px; height: 849px; overflow: hidden; }
  .front__photo {
    position: absolute; inset: 0;
    background:
      radial-gradient(ellipse 32% 30% at 22% 40%, var(--rock) 0%, rgba(196,96,47,0.6) 55%, rgba(196,96,47,0) 100%),
      radial-gradient(ellipse 12% 8% at 80% 57%, rgba(190,80,45,0.9) 0%, rgba(190,80,45,0) 100%),
      linear-gradient(180deg, var(--sky) 0%, #bfa2a3 14%, var(--peak) 22%, #b9a3ad 34%, #a99ca3 48%, var(--snow) 62%, #aba39c 76%, #8d8577 90%, #7d776d 100%);
  }
  .front__title {
    position: absolute; left: 66px; top: 588px; color: var(--paper);
    font-family: "Alegreya", Georgia, serif; font-weight: 800; line-height: 0.86;
  }
  .front__title-top { display: flex; align-items: flex-start; gap: 16px; }
  .front__word--lead { font-size: 103px; }
  .front__word--rest { display: block; font-size: 84px; margin-top: 6px; }
  .front__subtitle {
    margin-top: 18px; font: 400 22.5px/20.5px "Alegreya", Georgia, serif; letter-spacing: 0.3px;
  }
  .front__star { position: absolute; left: 430px; top: 748px; width: 28px; height: 36px; }
</style>
</head>
<body>
<main class="cover">
  <section class="back">
    <div class="back__photo" role="img" aria-label="Photo of red sandstone rocks before snowy pink mountain peaks at dawn"></div>
    <p class="back__intro">Lorem ipsum dolor sit amet, consectetuer adipiscing elit, sed diam nonummy nibh euismod tincidunt ut laoreet dolore magna aliquam erat volutpat. Ut wisi enim ad minim veniam, quis nostrud exerci tation ullamcorper suscipit lobortis nisl ut aliquip ex ea commodo consequat. Duis autem vel eum iriure dolor in hendrerit in vulputate velit esse molestie consequat, vel illum dolore eu</p>

    <svg class="divider divider--top" viewBox="0 0 374 18" aria-hidden="true">
      <polygon points="0,9 187,8.2 374,9 187,9.8" fill="var(--ink)"/>
      <path d="M187 0 Q188.4 7.6 193 9 Q188.4 10.4 187 18 Q185.6 10.4 181 9 Q185.6 7.6 187 0Z" fill="var(--ink)"/>
    </svg>
    <p class="back__quote back__quote--first">Lorem ipsum dolor sit amet,<br>consectetuer adipiscing elit,<br>sed diam nonummy nibh euis-<br>mod tincidunt ut laoreet<br>dolore magna aliquam erat<br>volutpat. Ut wisi enim ad</p>
    <svg class="divider divider--bottom" viewBox="0 0 374 18" aria-hidden="true">
      <polygon points="0,9 187,8.2 374,9 187,9.8" fill="var(--ink)"/>
      <path d="M187 0 Q188.4 7.6 193 9 Q188.4 10.4 187 18 Q185.6 10.4 181 9 Q185.6 7.6 187 0Z" fill="var(--ink)"/>
    </svg>
    <p class="back__quote back__quote--second">Ut wisi enim ad minim veniam,<br>quis nostrud exerci tation<br>ullamcorper suscipit lobortis</p>
  </section>

  <aside class="spine">
    <p class="spine__title">Pack Your Bags!The TOP holiday homes in Colorado</p>
    <svg class="spine__star" viewBox="0 0 16 16" aria-hidden="true">
      <path d="M8 0 Q9 7 16 8 Q9 9 8 16 Q7 9 0 8 Q7 7 8 0Z" fill="var(--coral)"/>
    </svg>
  </aside>

  <section class="front">
    <div class="front__photo" role="img" aria-label="Photo of red rock formations, snow-dusted scrub and a winding road beneath pink-lit snowy mountains"></div>
    <h1 class="front__title">
      <span class="front__title-top">
        <span class="front__word--lead">Pack</span>
        <span class="front__subtitle">The TOP<br>holiday homes<br>in Colorado</span>
      </span>
      <span class="front__word--rest">Your Bags!</span>
    </h1>
    <svg class="front__star" viewBox="0 0 28 36" aria-hidden="true">
      <path d="M14 0 Q15.5 15 28 18 Q15.5 21 14 36 Q12.5 21 0 18 Q12.5 15 14 0Z" fill="var(--paper)"/>
    </svg>
  </section>
</main>
</body>
</html>
```